Redesign of an insurance website

Attached is an insurance website that I need to redesign. Currently the website is too dark. I like for example www.brenvalo.com . Could you make the website lighter and change the structure a little so that it is more user friendly?

Industry/Entity Type

Insurance

Number of Pages Required

4 page

```html
<!DOCTYPE html>
<html lang="cs">
<head>
<meta charset="utf-8">
<title>JistotaPlus.cz</title>
<link href="https://fonts.googleapis.com/css2?family=Jost:wght@400;500;600&display=swap" rel="stylesheet">
<style>
:root{
  --blue:#2a7be4;
  --blue-light:#5fa2f7;
  --orange:#fb7d1d;
  --orange-soft:#fd9a48;
  --ink:#222;
  --grey:#444;
  --footer:#333;
  --white:#fff;
}
*{box-sizing:border-box;margin:0;padding:0}
html,body{width:837px;height:1200px;overflow:hidden;background:var(--white)}
body{position:relative;font-family:"Jost",sans-serif;color:var(--ink)}
.abs{position:absolute}
/* header */
.site-header{left:0;top:0;width:837px;height:35px;background:var(--white)}
.btn-small{display:flex;align-items:center;height:15px;font-size:9.5px;color:var(--white);padding-left:3px;top:10px}
.btn-small .arrow{width:13px;height:15px;margin-left:4px;display:flex;align-items:center;justify-content:center}
.btn-login{left:98px;background:var(--blue-light)}
.btn-login .arrow{background:var(--blue)}
.btn-register{left:179px;background:var(--orange-soft)}
.btn-register .arrow{background:var(--orange)}
.logo{left:0;width:837px;top:6px;text-align:center;font-weight:600;font-size:19px;letter-spacing:.5px;color:var(--blue)}
.main-nav{right:99px;top:14px;display:flex;gap:11px;font-size:10px}
.main-nav .active{color:var(--blue);border-bottom:1px solid var(--blue)}
/* hero */
.hero{left:0;top:35px;width:837px;height:394px;background:linear-gradient(100deg,#cfd2d4 0%,#a9aeb2 30%,#6d737a 48%,#2f3642 62%,#9d2a24 80%,#d8342c 100%)}
.picker{left:173px;top:259px;width:491px;height:170px;background:rgba(235,235,235,.88);border-radius:14px 14px 0 0}
.picker h2{position:absolute;top:15px;width:100%;text-align:center;font-weight:400;font-size:17px}
.chev{top:76px;font-size:18px;color:#777}
.option{top:54px;width:90px;text-align:center;font-size:8.5px;line-height:12px}
.option .ring{width:62px;height:62px;margin:0 auto 17px;border:1.5px solid var(--blue);border-radius:50%;display:flex;align-items:center;justify-content:center}
.option.selected{color:var(--orange)}
.option.selected .ring{background:var(--orange);border-color:var(--orange)}
/* why section */
.why-title{left:98px;top:488px;font-size:17px;color:var(--blue)}
.rule{height:1.5px;background:var(--orange)}
.benefits{left:98px;top:522px;list-style:none;font-size:12px;color:var(--grey)}
.benefits li{display:flex;align-items:center;height:24.7px}
.benefits svg{margin-right:7px}
.quote-form{left:505px;top:478px;width:233px;height:219px;background:var(--orange-soft);box-shadow:0 5px 6px rgba(0,0,0,.18)}
.quote-form h3{height:32px;background:var(--orange);color:var(--white);font-weight:400;font-size:12.5px;display:flex;align-items:center;justify-content:center}
.field{left:18px;width:196px;height:25px;border:1px solid #ffe1c4;border-radius:2px;font-size:8.5px;color:#ffe7d2;padding:6px 6px}
.consent{left:20px;top:161px;font-size:8.5px;color:var(--white);display:flex;align-items:center;gap:5px}
.btn-price{left:17px;top:186px;height:17px;background:var(--blue-light);color:var(--white);font-size:9.5px;display:flex;align-items:center;padding-left:4px}
.btn-price .arrow{background:var(--blue);width:17px;height:17px;margin-left:4px;display:flex;align-items:center;justify-content:center}
.form-brand{left:127px;top:189px;color:var(--white);font-weight:600;font-size:9.5px;letter-spacing:.5px}
/* offer section */
.offer-title{left:0;width:837px;top:742px;text-align:center;font-size:18px;color:var(--blue)}
.offer-image{left:97px;top:795px;width:275px;height:227px;border:2px solid #cfd2d4;background:linear-gradient(160deg,#8d96a0,#4d5865 60%,#5f6a74)}
.copy{left:405px;width:333px;font-size:9.5px;line-height:15.7px;color:var(--grey);letter-spacing:.15px}
.btn-save{left:405px;top:882px;height:17px;background:var(--orange-soft);color:var(--white);font-size:9px;display:flex;align-items:center;padding-left:4px}
.btn-save .arrow{background:var(--orange);width:16px;height:17px;margin-left:6px;display:flex;align-items:center;justify-content:center}
.how-title{left:405px;top:922px;font-size:13px;color:var(--blue)}
/* newsletter */
.newsletter{left:0;top:1076px;width:837px;height:86px;background:var(--blue-light)}
.newsletter h4{position:absolute;left:99px;top:34px;font-weight:400;font-size:15px;color:var(--white)}
.nl-input{left:283px;top:23px;width:355px;height:41px;background:#d7e6fc;border-radius:3px 0 0 3px;font-size:12px;font-style:italic;color:#9db4d6;padding:12px 17px}
.nl-submit{left:637px;top:23px;width:101px;height:41px;background:var(--orange);border-radius:0 3px 3px 0;color:var(--white);font-size:15px;display:flex;align-items:center;justify-content:center}
/* footer */
.site-footer{left:0;top:1162px;width:837px;height:38px;background:var(--footer)}
.footer-brand{left:100px;top:13px;color:#ddd;font-weight:600;font-size:12px;letter-spacing:.5px}
.social{top:10px;width:18px;height:18px;background:var(--orange)}
.legal{right:99px;top:4px;text-align:right;font-size:7.5px;line-height:15px;color:#ccc}
</style>
</head>
<body>

<header class="site-header abs">
  <div class="btn-small btn-login abs">PRIHLASIT SE<span class="arrow">→</span></div>
  <div class="btn-small btn-register abs">REGISTROVAT<span class="arrow">→</span></div>
  <div class="logo abs">JISTOTAPLUS.CZ</div>
  <nav class="main-nav abs"><span class="active">O NAS</span><span>CASTE DOTAZY</span><span>KONTAKT</span></nav>
</header>

<section class="hero abs" role="img" aria-label="Fotografie: dva řidiči se dohadují u poškozených aut po nehodě"></section>

<div class="picker abs">
  <h2>CHCETE POJISTIT NECO JINEHO ?</h2>
  <span class="chev abs" style="left:32px">‹</span>
  <span class="chev abs" style="left:455px">›</span>
  <div class="option selected abs" style="left:46px">
    <div class="ring"><svg width="34" height="22" viewBox="0 0 34 22"><g fill="none" stroke="#fff" stroke-width="2"><rect x="2" y="8" width="16" height="8" rx="2"/><path d="M5 8l2-5h6l2 5"/><rect x="15" y="10" width="16" height="8" rx="2"/><path d="M18 10l2-5h6l2 5"/></g></svg></div>
    Lorem Ipsum<br>aorsum
  </div>
  <div class="option abs" style="left:148px">
    <div class="ring"><svg width="28" height="28" viewBox="0 0 24 24"><path fill="var(--blue)" d="M21 16v-2l-8-5V3.5a1.5 1.5 0 0 0-3 0V9l-8 5v2l8-2.5V19l-2 1.5V22l3.5-1 3.5 1v-1.5L13 19v-5.5z" transform="rotate(45 12 12)"/></svg></div>
    Lorem Ipsum<br>aorsum
  </div>
  <div class="option abs" style="left:251px">
    <div class="ring"><svg width="26" height="24" viewBox="0 0 24 22"><path fill="var(--blue)" d="M12 2L1 12h3v9h6v-6h4v6h6v-9h3z"/></svg></div>
    Lorem Ipsum<br>aorsum
  </div>
  <div class="option abs" style="left:354px">
    <div class="ring"><svg width="32" height="14" viewBox="0 0 32 14"><path fill="var(--blue)" d="M2 7l5-1 4-4h9l5 4 5 1v4H2z"/><circle cx="9" cy="11" r="2.5" fill="#fff" stroke="var(--blue)"/><circle cx="24" cy="11" r="2.5" fill="#fff" stroke="var(--blue)"/></svg></div>
    Lorem Ipsum<br>aorsum
  </div>
</div>

<h2 class="why-title abs" style="font-weight:400">PROC HLEDAT POJISTENI PRES JISTOTAPLUS.CZ?</h2>
<div class="rule abs" style="left:98px;top:512px;width:74px"></div>
<ul class="benefits abs">
  <li><svg width="11" height="11" viewBox="0 0 11 11"><rect x=".75" y="1.75" width="8.5" height="8.5" fill="none" stroke="var(--blue)" stroke-width="1.5"/><path d="M3 5.5l2 2L10.5 1" fill="none" stroke="var(--blue)" stroke-width="1.8"/></svg>s námi najdete tu nejvýhodnější nabídku</li>
  <li><svg width="11" height="11" viewBox="0 0 11 11"><rect x=".75" y="1.75" width="8.5" height="8.5" fill="none" stroke="var(--blue)" stroke-width="1.5"/><path d="M3 5.5l2 2L10.5 1" fill="none" stroke="var(--blue)" stroke-width="1.8"/></svg>zaručíme vám nejlepší cenu na trhu</li>
  <li><svg width="11" height="11" viewBox="0 0 11 11"><rect x=".75" y="1.75" width="8.5" height="8.5" fill="none" stroke="var(--blue)" stroke-width="1.5"/><path d="M3 5.5l2 2L10.5 1" fill="none" stroke="var(--blue)" stroke-width="1.8"/></svg>stačí pár minut a můžete ušetřit tisíce</li>
  <li><svg width="11" height="11" viewBox="0 0 11 11"><rect x=".75" y="1.75" width="8.5" height="8.5" fill="none" stroke="var(--blue)" stroke-width="1.5"/><path d="M3 5.5l2 2L10.5 1" fill="none" stroke="var(--blue)" stroke-width="1.8"/></svg>srovnáváme všechny pojišťovny</li>
  <li><svg width="11" height="11" viewBox="0 0 11 11"><rect x=".75" y="1.75" width="8.5" height="8.5" fill="none" stroke="var(--blue)" stroke-width="1.5"/><path d="M3 5.5l2 2L10.5 1" fill="none" stroke="var(--blue)" stroke-width="1.8"/></svg>zařídíme vám všechny druhy pojištění</li>
  <li><svg width="11" height="11" viewBox="0 0 11 11"><rect x=".75" y="1.75" width="8.5" height="8.5" fill="none" stroke="var(--blue)" stroke-width="1.5"/><path d="M3 5.5l2 2L10.5 1" fill="none" stroke="var(--blue)" stroke-width="1.8"/></svg>vše vyřídíte z pohodlí domova</li>
  <li><svg width="11" height="11" viewBox="0 0 11 11"><rect x=".75" y="1.75" width="8.5" height="8.5" fill="none" stroke="var(--blue)" stroke-width="1.5"/><path d="M3 5.5l2 2L10.5 1" fill="none" stroke="var(--blue)" stroke-width="1.8"/></svg>nemusíte nikam chodit a ušetříte</li>
</ul>

<form class="quote-form abs">
  <h3>NAJDETE NEJVYHODNEJSI POJISTENI</h3>
  <div class="field abs" style="top:45px">Jmeno</div>
  <div class="field abs" style="top:83px">Prijmeni</div>
  <div class="field abs" style="top:122px">E-mail</div>
  <div class="consent abs"><svg width="10" height="10" viewBox="0 0 11 11"><rect x=".75" y="1.75" width="8.5" height="8.5" fill="none" stroke="#fff" stroke-width="1.2"/><path d="M3 5.5l2 2L10.5 1" fill="none" stroke="#fff" stroke-width="1.4"/></svg>Souhlasím s podmínkami použití</div>
  <div class="btn-price abs">SPOCITAT CENU<span class="arrow">→</span></div>
  <div class="form-brand abs">JISTOTAPLUS.CZ</div>
</form>

<h2 class="offer-title abs" style="font-weight:400">UZAVŘELI JSTE V MINULOSTI NEVÝHODNOU POJISTKU? ZBAVTE SE JÍ!</h2>
<div class="rule abs" style="left:382px;top:768px;width:73px"></div>

<div class="offer-image abs" role="img" aria-label="Ilustrace: dlaně chránící nakreslený domek před deštěm z mraků"></div>

<p class="copy abs" style="top:785px">Máte pocit, že za stávající pojištění platíte příliš? Teď za své peníze dostanete více. Pojďte něco udělat. S námi najdete tu nejvýhodnější nabídku na trhu a nebudete ji dlouho hledat. Je to nejsnazší způsob, jak se zbavit starého nevýhodného pojištění. Stačí kliknout a vydat se na cestu k levnějšímu pojištění.</p>
<div class="btn-save abs">CHCI USETRIT<span class="arrow">→</span></div>

<h3 class="how-title abs" style="font-weight:400">JAK TO FUNGUJE</h3>
<div class="rule abs" style="left:405px;top:942px;width:73px"></div>
<p class="copy abs" style="top:953px">Lorem ipsum dolor sit amet, consectetuer adipiscing elit, sed diam nonummy nibh euismod tincidunt ut laoreet dolore magna aliquam erat volutpat. Ut wisi enim ad minim veniam, quis nostrud exerci tation ullamcorper suscipit lobortis nisl ut aliquip ex ea commodo consequat. Duis autem vel eum iriure dolor in hendrerit in vulputate.</p>

<section class="newsletter abs">
  <h4>ODEBIRAT NEWLETTER</h4>
  <div class="nl-input abs">E-mail</div>
  <div class="nl-submit abs">POTVRDIT</div>
</section>

<footer class="site-footer abs">
  <div class="footer-brand abs">JISTOTAPLUS.CZ</div>
  <span class="social abs" style="left:381px" aria-label="Sociální síť"></span>
  <span class="social abs" style="left:409px" aria-label="Sociální síť"></span>
  <span class="social abs" style="left:437px" aria-label="Sociální síť"></span>
  <div class="legal abs">Ochrana soukromí | Podmínky použití<br>Copyright © 2017 JistotaPlus.cz. Všechna práva vyhrazena.</div>
</footer>

</body>
</html>
```